Visitenkarten-Design für Recommerce Unternehmen
Zielgruppe
Recommerce Unternehmen für Porzellan, Glas, Besteck. Wir handeln mit hochwertigen ausgelaufenen Artikeln und ermöglichen unseren Kunden den Nachkauf gesuchter Stücke.
Aufgabenstellung
Möglichst gleiches Look and Feel von der Homepage verwenden, aber darf gern ein wenig Frische reinbringen.

```html
<!DOCTYPE html>
<html lang="de">
<head>
<meta charset="utf-8">
<title>Tassenfund – Visitenkarte</title>
<link href="https://fonts.googleapis.com/css2?family=Arvo&family=Roboto:wght@300&family=Roboto+Slab:wght@600;700&display=swap" rel="stylesheet">
<style>
  :root {
    --stage: #f1f2f3;
    --card-tint: #e8eef3;
    --white: #ffffff;
    --porcelain-blue: #a9bfe0;
    --brand-blue: #1f6496;
    --ink: #2f3438;
    --slate: #3e4c55;
    --text: #1e2326;
  }
  * { margin: 0; padding: 0; box-sizing: border-box; }
  html, body { width: 1200px; height: 1080px; overflow: hidden; }
  body { background: var(--stage); position: relative; }

  .card { position: absolute; left: 300px; width: 627px; height: 406px; overflow: hidden; }

  /* Vorderseite */
  .card-front { top: 91px; background: var(--card-tint); }
  .front-brand { position: absolute; left: 0; right: 0; top: 150px; transform: translateY(-50%);
    display: flex; align-items: center; justify-content: center; gap: 22px; }
  .brand-dot { width: 74px; height: 74px; border-radius: 50%; background: var(--porcelain-blue); }
  .brand-name { font-family: "Roboto Slab", serif; font-weight: 700; color: var(--ink); }
  .front-brand .brand-name { font-size: 62px; }
  .front-band { position: absolute; left: 0; right: 0; top: 256px; height: 13px; background: var(--porcelain-blue); }
  .front-panel { position: absolute; left: 19px; right: 18px; top: 287px; bottom: 0;
    background: var(--white); border-radius: 12px 12px 0 0; text-align: center; }
  .tagline-intro { font-family: "Roboto", sans-serif; font-weight: 300; font-size: 22px; color: var(--slate); margin-top: 16px; }
  .tagline-range { font-family: "Roboto Slab", serif; font-weight: 600; font-size: 23px; color: var(--slate); margin-top: 2px; }
  .front-url { font-family: "Roboto Slab", serif; font-weight: 700; font-size: 22px; color: var(--brand-blue); margin-top: 14px; }

  /* Rückseite */
  .card-back { top: 562px; background: var(--card-tint); }
  .back-logo-side { position: absolute; left: 0; top: 0; bottom: 0; width: 238px; background: var(--white); }
  .back-brand { position: absolute; left: 24px; top: 192px; display: flex; align-items: center; gap: 10px; }
  .back-brand .brand-dot { width: 36px; height: 36px; }
  .back-brand .brand-name { font-size: 26px; }
  .company { position: absolute; left: 283px; top: 26px; font-family: "Arvo", serif; font-size: 17px; color: var(--text); }
  .slogan { position: absolute; left: 200px; top: 62px; width: 424px; height: 105px;
    background: var(--porcelain-blue); border-radius: 8px; padding: 24px 0 0 12px;
    font-family: "Roboto Slab", serif; font-weight: 600; font-size: 19.5px; line-height: 33px; color: var(--brand-blue); }
  .contact { position: absolute; left: 284px; font-family: "Arvo", serif; font-size: 17px; line-height: 29px; color: var(--text); }
  .contact-address { top: 183px; }
  .contact-phone { top: 257px; }
  .contact-web { top: 327px; }
  .contact-label { color: var(--brand-blue); display: inline-block; width: 24px; }
</style>
</head>
<body>
  <section class="card card-front">
    <div class="front-brand">
      <span class="brand-dot"></span>
      <span class="brand-name">Tassenfund</span>
    </div>
    <div class="front-band"></div>
    <div class="front-panel">
      <p class="tagline-intro">Onlinebörse für</p>
      <p class="tagline-range">Porzellan, Besteck und Glaswaren</p>
      <p class="front-url">www.tassenfund.de</p>
    </div>
  </section>

  <section class="card card-back">
    <div class="back-logo-side">
      <div class="back-brand">
        <span class="brand-dot"></span>
        <span class="brand-name">Tassenfund</span>
      </div>
    </div>
    <p class="company">Porzellanbörse tassenfund.de GmbH</p>
    <div class="slogan">
      <p>Haben Sie nicht alle Tassen im Schrank?</p>
      <p>Oder zu viele Teller im Keller?</p>
    </div>
    <address class="contact contact-address" style="font-style:normal">
      Mühlenkamp 58<br>21029 Hamburg
    </address>
    <p class="contact contact-phone">
      <span class="contact-label">T</span>040 718 36 52 - 00<br>
      <span class="contact-label">F</span>040 718 36 52 - 29
    </p>
    <p class="contact contact-web">info@tassenfund.de<br>www.tassenfund.de</p>
  </section>
</body>
</html>
```